Business Card Redesign

We would like to redesign our existing business cards.
The new design shall look:
ELEGANT, LUXURY, PROFESSIONAL
Reference:
YOU CAN VISIT WWW.LUMEN-BRIDGE-PARTNERS.EXAMPLE FOR BETTER UNDERSTANDING OF COMPANY STRATEGY AND POSITION
Additional:
CHOSEN CANDIDATE SHALL PROVIDE THE INSTRUCTION OF PRINTING IF ANY THERMAL COVERAGE OR ANY ADDITION IS OFFERED
Industry/Entity Type
Business

```html
<!DOCTYPE html>
<html lang="en">
<head>
<meta charset="utf-8">
<title>Lumen Bridge Partners – Business Card</title>
<link rel="stylesheet" href="https://fonts.googleapis.com/css2?family=PT+Sans:wght@400&family=Questrial&family=Noto+Sans+TC:wght@400;700&display=swap">
<style>
  :root {
    --page: #f2f4f7;
    --sky: #1fc6f4;
    --ocean: #1a72c0;
    --deep: #1d4f9c;
    --navy: #1f2a6b;
    --seal: #0f4f8f;
    --gold: #f2a81c;
    --white: #ffffff;
  }
  * { margin: 0; padding: 0; box-sizing: border-box; }
  html, body { width: 832px; height: 1200px; overflow: hidden; background: var(--page); }
  .canvas { position: relative; width: 832px; height: 1200px; }

  .card {
    position: absolute;
    left: 16px;
    width: 800px;
    height: 476px;
    color: var(--white);
    background: linear-gradient(135deg, var(--sky) 0%, var(--ocean) 45%, var(--deep) 72%, var(--navy) 100%);
    overflow: hidden;
  }
  .card--front { top: 70px; font-family: "PT Sans", sans-serif; }
  .card--back { top: 660px; font-family: "Questrial", "Noto Sans TC", sans-serif; }

  /* brand lockup */
  .brand { position: absolute; display: flex; flex-direction: column; align-items: center; text-align: center; }
  .brand__dot { width: 96px; height: 96px; border-radius: 50%; background: var(--seal); margin-bottom: 22px; }
  .brand__name { font-size: 30px; line-height: 1.2; letter-spacing: 2px; color: var(--white); }
  .card--front .brand { left: 30px; top: 120px; width: 400px; }
  .card--back .brand { left: 470px; top: 120px; width: 310px; }
  .card--back .brand__name { font-family: "PT Sans", sans-serif; font-size: 24px; }

  /* front details */
  .details { position: absolute; left: 450px; top: 52px; width: 345px; white-space: nowrap; }
  .details__name { font-size: 40px; line-height: 1; margin-bottom: 12px; }
  .details__role { font-size: 20px; line-height: 24px; margin-bottom: 20px; }
  .details__row { font-size: 20px; line-height: 30px; }
  .details__label { display: inline-block; width: 74px; }
  .details__hq { font-size: 20px; line-height: 24px; margin-top: 18px; }
  .details__address { font-size: 20px; line-height: 25px; margin-top: 4px; }
  .details__web { font-size: 20px; line-height: 25px; margin-top: 8px; }
  .details__lines { font-size: 20px; line-height: 25px; margin-top: 12px; }

  /* back details */
  .zh-company { position: absolute; left: 40px; top: 30px; font-family: "Noto Sans TC", sans-serif; font-weight: 700; font-size: 28px; letter-spacing: 3px; color: var(--gold); }
  .zh-name { position: absolute; left: 40px; top: 92px; font-family: "Noto Sans TC", sans-serif; font-size: 40px; letter-spacing: 4px; color: var(--gold); }
  .zh-role { position: absolute; left: 40px; top: 150px; font-family: "Noto Sans TC", sans-serif; font-size: 22px; letter-spacing: 3px; }
  .zh-contact { position: absolute; left: 40px; top: 196px; font-size: 21px; line-height: 32px; letter-spacing: 1px; white-space: nowrap; }
  .zh-contact__label { display: inline-block; width: 86px; font-family: "Noto Sans TC", sans-serif; letter-spacing: 6px; }
  .zh-hq { position: absolute; left: 40px; top: 318px; font-family: "Noto Sans TC", sans-serif; font-size: 18px; letter-spacing: 4px; color: var(--gold); }
  .zh-address { position: absolute; left: 40px; top: 344px; font-size: 21px; line-height: 28px; letter-spacing: 2px; white-space: nowrap; }
  .zh-lines { position: absolute; left: 428px; top: 344px; font-size: 21px; line-height: 28px; letter-spacing: 1px; white-space: nowrap; }
  .zh-web { position: absolute; left: 36px; top: 426px; font-size: 20px; color: var(--gold); white-space: nowrap; }
</style>
</head>
<body>
<main class="canvas">

  <section class="card card--front" aria-label="Business card, English side">
    <div class="brand">
      <span class="brand__dot"></span>
      <span class="brand__name">LUMEN BRIDGE<br>PARTNERS LIMITED</span>
    </div>
    <div class="details">
      <p class="details__name">Marisa Lowe</p>
      <p class="details__role">PR Consultant</p>
      <p class="details__row"><span class="details__label">E-mail</span>marisa@lbpartners.example</p>
      <p class="details__row"><span class="details__label">Mobile</span>(852) 5550 0142</p>
      <p class="details__hq">Headquarters (Hong Kong)</p>
      <p class="details__address">Rm. 808B, 8/F, Harbourlight Centre,<br>17 Example Road, Central,<br>Hong Kong</p>
      <p class="details__web">www.lumen-bridge-partners.example</p>
      <p class="details__lines">Tel: (852) 2555-0100<br>Fax: (852) 2555-0101</p>
    </div>
  </section>

  <section class="card card--back" aria-label="Business card, Chinese side">
    <p class="zh-company">明橋顧問有限公司</p>
    <p class="zh-name">盧美莎</p>
    <p class="zh-role">公關顧問</p>
    <div class="zh-contact">
      <p><span class="zh-contact__label">電郵:</span>marisa@lbpartners.example</p>
      <p><span class="zh-contact__label">手提:</span>(852) 5550 0142</p>
    </div>
    <p class="zh-hq">香港總部</p>
    <p class="zh-address">香港中環範例道17號<br>港光中心8樓808B</p>
    <p class="zh-lines">電話 : (852) 2555-0100<br>傳真 : (852) 2555-0101</p>
    <p class="zh-web">www.lumen-bridge-partners.example</p>
    <div class="brand">
      <span class="brand__dot"></span>
      <span class="brand__name">LUMEN BRIDGE<br>PARTNERS LIMITED</span>
    </div>
  </section>

</main>
</body>
</html>
```